Event Graphics for a Summer Camp for Middle School and High School Students

I need graphics designed for our summer camps event. These camps are for teenagers, 6-12th grades. Primary graphic design is for a 11x17 poster but will also need the images resized for:
-social media
-16x9 title slide
- a postcard size
Graphic should include the following:
-Main Title: RV Pathlight presents . . . Summer Camp
-Dates: Kindle - June 3-7, High School - June 8-12, Middle School - June 22-26
-Register at RVPathlight.com
-Maple Crest Retreat Center, Deadwood, SD
-For each camp, include name and headshot of speaker: Kindle: Tom Wakeley (black jacket photo), High: Luis Ortega (hispanic man), Middle: Barrington Pope (tan shirt). Gave some options for headshots. Use what works best for cropping.
-Include RV Pathlight logo
-Event Graphic should be attractive to teenagers. Open to ideas
My graphic design experience is limited. I will need help receiving the files I need in the various sizes. Thank you.

```html
<!DOCTYPE html>
<html lang="en">
<head>
<meta charset="utf-8">
<title>RV Pathlight Summer Camps 2020</title>
<link href="https://fonts.googleapis.com/css2?family=Montserrat:wght@700;800;900&display=swap" rel="stylesheet">
<style>
  :root {
    --sky-top: #1f1d4a;
    --sky-mid: #4b2f72;
    --sky-glow: #c8566a;
    --horizon: #f08a4b;
    --forest: #141628;
    --ice: #8fd3f4;
    --ice-dark: #1b4f8a;
    --white: #ffffff;
    --orange: #f5891f;
    --orange-dark: #c4581a;
    --band: #14284f;
    --portrait-a: #3b3f5c;
    --portrait-b: #a7a2b5;
  }
  * { margin: 0; padding: 0; box-sizing: border-box; }
  html, body { width: 778px; height: 1200px; overflow: hidden; }
  body { font-family: "Montserrat", sans-serif; }

  .poster {
    position: relative;
    width: 778px;
    height: 1200px;
    overflow: hidden;
    background: linear-gradient(180deg, var(--sky-top) 0%, var(--sky-mid) 45%, var(--sky-glow) 68%, var(--horizon) 80%);
  }
  .forest {
    position: absolute;
    left: 0; bottom: 0;
    width: 778px; height: 360px;
    background: linear-gradient(180deg, rgba(20,22,40,0) 0%, rgba(20,22,40,.85) 30%, var(--forest) 60%);
  }

  .brand {
    position: absolute;
    left: 18px; top: 34px;
    width: 200px;
    color: var(--white);
    font-weight: 900;
    font-size: 32px;
    line-height: 1.05;
  }

  .title { position: absolute; left: 0; top: 0; }
  .title text { font-family: "Montserrat", sans-serif; font-weight: 900; }
  .title-summer { fill: var(--ice); stroke: var(--ice-dark); stroke-width: 8; paint-order: stroke; stroke-linejoin: round; }
  .title-camps { fill: var(--white); }
  .title-year { fill: var(--orange); }

  .camp-label {
    position: absolute;
    color: var(--white);
    font-weight: 800;
    font-size: 30px;
    line-height: 1;
    transform: translateX(-50%);
  }
  .camp-label.kindle { left: 160px; top: 316px; }
  .camp-label.high { left: 610px; top: 316px; }
  .camp-label.middle { left: 389px; top: 546px; }

  .badges { position: absolute; left: 0; top: 0; }
  .badge-text { font-family: "Montserrat", sans-serif; font-weight: 800; fill: var(--band); }

  .register-stamp {
    position: absolute;
    left: 536px; top: 928px;
    width: 224px; height: 150px;
    transform: rotate(-15deg);
    background: var(--orange);
    border: 5px solid var(--orange-dark);
    border-radius: 10px;
    box-shadow: inset 0 0 0 4px var(--orange), inset 0 0 0 7px var(--white);
    display: flex;
    flex-direction: column;
    align-items: center;
    justify-content: center;
    color: var(--white);
    font-weight: 900;
    text-align: center;
  }
  .register-stamp .lead { font-size: 28px; line-height: 1.1; }
  .register-stamp .site { font-size: 22px; line-height: 1.2; }

  .venue-band {
    position: absolute;
    left: 0; bottom: 0;
    width: 778px; height: 66px;
    background: var(--band);
    color: var(--white);
    font-weight: 800;
    font-size: 27px;
    display: flex;
    align-items: center;
    justify-content: center;
  }
</style>
</head>
<body>
<main class="poster">
  <div class="forest" role="img" aria-label="Silhouette of pine trees against a sunset horizon"></div>

  <div class="brand">RV<br>Pathlight</div>

  <svg class="title" width="778" height="270" viewBox="0 0 778 270" role="heading" aria-level="1" aria-label="Summer Camps 2020">
    <text class="title-summer" x="240" y="150" font-size="118" textLength="515" lengthAdjust="spacingAndGlyphs">SUMMER</text>
    <text class="title-camps" x="228" y="248" font-size="90" textLength="335" lengthAdjust="spacingAndGlyphs">CAMPS</text>
    <text class="title-year" x="580" y="246" font-size="52" textLength="150" lengthAdjust="spacingAndGlyphs">2020</text>
  </svg>

  <div class="camp-label kindle">Kindle</div>
  <div class="camp-label high">High</div>
  <div class="camp-label middle">Middle</div>

  <svg class="badges" width="778" height="1200" viewBox="0 0 778 1200">
    <defs>
      <radialGradient id="portrait-fill" cx="50%" cy="40%" r="60%">
        <stop offset="0%" stop-color="#a7a2b5"/>
        <stop offset="100%" stop-color="#3b3f5c"/>
      </radialGradient>
      <path id="arc-kindle-top" d="M 60 485 A 100 100 0 0 1 260 485"/>
      <path id="arc-kindle-bot" d="M 58 485 A 102 102 0 0 0 262 485"/>
      <path id="arc-high-top" d="M 510 485 A 100 100 0 0 1 710 485"/>
      <path id="arc-high-bot" d="M 508 485 A 102 102 0 0 0 712 485"/>
      <path id="arc-middle-top" d="M 299 705 A 90 90 0 0 1 479 705"/>
      <path id="arc-middle-bot" d="M 297 705 A 92 92 0 0 0 481 705"/>
    </defs>

    <g class="badge kindle">
      <circle cx="160" cy="485" r="132" fill="#ffffff"/>
      <circle cx="160" cy="485" r="124" fill="none" stroke="#14284f" stroke-width="2" stroke-dasharray="4 5"/>
      <circle cx="160" cy="485" r="92" fill="url(#portrait-fill)" role="img" aria-label="Headshot of speaker Tom Wakeley"/>
      <text class="badge-text" font-size="24"><textPath href="#arc-kindle-top" startOffset="50%" text-anchor="middle">June 3-7</textPath></text>
      <text class="badge-text" font-size="21" dominant-baseline="hanging"><textPath href="#arc-kindle-bot" startOffset="50%" text-anchor="middle">Tom Wakeley</textPath></text>
    </g>

    <g class="badge high">
      <circle cx="610" cy="485" r="132" fill="#ffffff"/>
      <circle cx="610" cy="485" r="124" fill="none" stroke="#14284f" stroke-width="2" stroke-dasharray="4 5"/>
      <circle cx="610" cy="485" r="92" fill="url(#portrait-fill)" role="img" aria-label="Headshot of speaker Luis Ortega"/>
      <text class="badge-text" font-size="24"><textPath href="#arc-high-top" startOffset="50%" text-anchor="middle">June 8-12</textPath></text>
      <text class="badge-text" font-size="21" dominant-baseline="hanging"><textPath href="#arc-high-bot" startOffset="50%" text-anchor="middle">Luis Ortega</textPath></text>
    </g>

    <g class="badge middle">
      <circle cx="389" cy="705" r="120" fill="#ffffff"/>
      <circle cx="389" cy="705" r="112" fill="none" stroke="#14284f" stroke-width="2" stroke-dasharray="4 5"/>
      <circle cx="389" cy="705" r="82" fill="url(#portrait-fill)" role="img" aria-label="Headshot of speaker Barrington Pope"/>
      <text class="badge-text" font-size="22"><textPath href="#arc-middle-top" startOffset="50%" text-anchor="middle">June 22-26</textPath></text>
      <text class="badge-text" font-size="19" dominant-baseline="hanging"><textPath href="#arc-middle-bot" startOffset="50%" text-anchor="middle">Barrington Pope</textPath></text>
    </g>
  </svg>

  <div class="register-stamp">
    <span class="lead">Register at</span>
    <span class="site">RVPathlight.com</span>
  </div>

  <footer class="venue-band">Maple Crest Retreat Center, Deadwood, SD</footer>
</main>
</body>
</html>
```